A label for my commercially sold local honey. This is a LABEL not a logo

3 inches high
2 inches wide

Target Market(s)

Customers who like "local" honey

Logo Text

Wildflower Honey -- 100% Pure & Unfiltered -- Florida

Logo styles of interest
Wordmark Logo
Requirements
Must have
• Wildflower Honey -- 100% Pure & Unfiltered -- Florida

Florida should be dominant

3 inches high / 2 inches wide

```html
<!DOCTYPE html>
<html lang="en">
<head>
<meta charset="utf-8">
<title>Wildflower Honey Label</title>
<link href="https://fonts.googleapis.com/css2?family=Oranienbaum&family=Caveat+Brush&family=Montserrat:wght@400;600&family=Playfair+Display:wght@900&display=swap" rel="stylesheet">
<style>
  :root {
    --page: #ffffff;
    --honey-light: #fbd84a;
    --honey: #f7c51e;
    --honey-deep: #f2b705;
    --ink: #2e2d30;
    --white: #ffffff;
    --gold-line: #f5c400;
  }
  html, body {
    margin: 0;
    padding: 0;
    width: 1200px;
    height: 846px;
    overflow: hidden;
    background: var(--page);
  }
  .canvas {
    position: relative;
    width: 1200px;
    height: 846px;
  }
  .label {
    position: absolute;
    left: 410px;
    top: 86px;
    width: 380px;
    height: 673px;
  }
  .label-ground {
    position: absolute;
    inset: 0;
    background: linear-gradient(160deg, var(--honey-light) 0%, var(--honey) 55%, var(--honey-deep) 100%);
  }
  .product-kind {
    position: absolute;
    top: 34px;
    left: 0;
    width: 100%;
    margin: 0;
    text-align: center;
    font-family: "Oranienbaum", serif;
    font-size: 46px;
    line-height: 1;
    color: var(--ink);
    letter-spacing: 1px;
  }
  .product-name {
    position: absolute;
    top: 82px;
    left: 0;
    width: 100%;
    display: flex;
    justify-content: center;
    align-items: center;
    font-family: "Oranienbaum", serif;
    font-size: 104px;
    font-weight: 400;
    line-height: 1;
    color: var(--ink);
    margin: 0;
  }
  .bee-mark {
    display: inline-block;
    width: 92px;
    height: 72px;
    margin: 0 2px;
    border-radius: 46px 46px 40px 40px;
    background: linear-gradient(180deg, var(--white) 0%, var(--honey) 60%, var(--ink) 100%);
  }
  .purity-badge {
    position: absolute;
    left: -35px;
    top: 178px;
    width: 450px;
    height: 285px;
    overflow: visible;
  }
  .purity-figure {
    position: absolute;
    top: 250px;
    left: 0;
    width: 100%;
    text-align: center;
    font-family: "Caveat Brush", cursive;
    font-size: 96px;
    line-height: 1;
    color: var(--white);
    margin: 0;
  }
  .purity-claim {
    position: absolute;
    top: 336px;
    left: 0;
    width: 100%;
    text-align: center;
    font-family: "Montserrat", sans-serif;
    font-weight: 400;
    font-size: 22px;
    line-height: 26px;
    color: var(--white);
    margin: 0;
  }
  .purity-claim .amp { font-size: 17px; }
  .origin {
    position: absolute;
    top: 456px;
    left: 0;
    width: 100%;
    text-align: center;
    font-family: "Playfair Display", serif;
    font-weight: 900;
    font-size: 80px;
    line-height: 1;
    color: var(--ink);
    margin: 0;
    transform: scaleX(0.78);
    text-shadow: -3px 3px 0 var(--white), -5px 6px 6px rgba(0, 0, 0, 0.25);
  }
  .maker-seal {
    position: absolute;
    left: 144px;
    top: 560px;
    width: 92px;
    height: 100px;
  }
  .maker-name {
    position: absolute;
    left: 144px;
    top: 560px;
    width: 92px;
    height: 100px;
    display: flex;
    align-items: center;
    justify-content: center;
    text-align: center;
    font-family: "Montserrat", sans-serif;
    font-weight: 600;
    font-size: 12px;
    line-height: 15px;
    color: var(--ink);
    margin: 0;
  }
</style>
</head>
<body>
<main class="canvas">
  <section class="label">
    <div class="label-ground" role="img" aria-label="Honeycomb pattern in golden yellow tones"></div>

    <p class="product-kind">WILDFLOWER</p>
    <h1 class="product-name">H<span class="bee-mark" role="img" aria-label="Bee illustration standing in for the letter O"></span>NEY</h1>

    <svg class="purity-badge" viewBox="0 0 450 285" aria-hidden="true">
      <polygon points="225,10 440,142.5 225,275 10,142.5" fill="#2e2d30" stroke="#2e2d30" stroke-width="20" stroke-linejoin="round"/>
      <polygon points="225,26 412,142.5 225,259 38,142.5" fill="none" stroke="#f5c400" stroke-width="3"/>
    </svg>
    <p class="purity-figure">100%</p>
    <p class="purity-claim">Pure <span class="amp">&amp;</span><br>Unfiltered</p>

    <h2 class="origin">FLORIDA</h2>

    <svg class="maker-seal" viewBox="0 0 92 100" aria-hidden="true">
      <polygon points="46,2 89,26 89,74 46,98 3,74 3,26" fill="#ffffff"/>
    </svg>
    <p class="maker-name">Grove<br>Market</p>
  </section>
</main>
</body>
</html>
```